International Sex Coach needs a Book Cover in less than 3 days

I need a cover design for my book coming out next week titled "The Open Map of Desire". The book explores the origins of our cultural ideas about sexuality and taboo and is interwoven with personal memoir.
The reader must feel that they are being pulled into an intimate sexual story, but also a deeper understanding of sex itself. Like they are jumping into bed with me, you might say. I would like the title to take up the majority of the space over an image of 3D, very real bed sheets, but I am open to your ideas. I haven't purchased any images yet, but there are a few below I was drawn to.
In its essence, this book is designed to reeducate the reader about sexuality and open them up to a new paradigm of sexual wellness.
The author name is Marisa Tolven. Page must also include the phrase: a radical fresh perspective on intimacy, partnership and love.
Size 6" x 9" (15.24 x 22.86 cm)
Thanks!
Updates

Target Market(s)

Sexually active men and women.

Industry/Entity Type

Wellness

Font styles to use
Serif

```html
<!DOCTYPE html>
<html lang="en">
<head>
<meta charset="utf-8">
<title>The Open Map of Desire — Cover Wrap</title>
<link rel="stylesheet" href="https://fonts.googleapis.com/css2?family=Anton&family=Libre+Baskerville&display=swap">
<style>
  :root {
    --sheet-light: #fbf7ea;
    --sheet-mid: #f1e9d0;
    --sheet-shadow: #ddd0ab;
    --skin-tint: #e8c3c6;
    --ink: #1a1a1a;
    --magenta: #c93fdc;
    --plum: #5b1f63;
    --band-1: #9a3aa8;
    --band-2: #b04cc0;
    --band-3: #c860d6;
    --white: #ffffff;
  }
  * { margin: 0; padding: 0; box-sizing: border-box; }
  html, body { width: 1200px; height: 819px; overflow: hidden; background: var(--sheet-light); }
  .cover-wrap { position: relative; width: 1200px; height: 819px; overflow: hidden; }

  .sheets-photo {
    position: absolute; inset: 0;
    background:
      radial-gradient(ellipse 260px 240px at 960px 170px, rgba(232,195,198,0.8), rgba(232,195,198,0) 70%),
      linear-gradient(115deg, var(--sheet-mid) 0%, var(--sheet-light) 30%, var(--sheet-shadow) 45%, var(--sheet-light) 60%, var(--sheet-mid) 80%, var(--sheet-light) 100%);
  }

  /* Spine */
  .spine-title-block {
    position: absolute; left: 560px; top: 30px; height: 570px;
    writing-mode: vertical-rl;
  }
  .spine-title {
    font-family: "Anton", Impact, sans-serif;
    font-size: 40px; line-height: 44px; color: var(--ink); letter-spacing: 0.5px;
    display: block;
  }
  .spine-title .accent { color: var(--magenta); }
  .spine-tagline {
    font-family: "Libre Baskerville", Georgia, serif;
    font-size: 16px; line-height: 20px; color: var(--ink);
    display: block;
  }
  .spine-author-box {
    position: absolute; left: 555px; top: 606px; width: 90px; height: 213px;
    background: var(--plum); border-radius: 16px 16px 0 0; overflow: hidden;
  }
  .spine-author-box .band { position: absolute; top: 0; bottom: 0; width: 10px; }
  .band.b1 { left: 0; background: var(--band-3); }
  .band.b2 { left: 10px; background: var(--band-2); }
  .band.b3 { left: 20px; background: var(--band-1); }
  .spine-author {
    position: absolute; left: 32px; top: 14px;
    writing-mode: vertical-rl;
    font-family: "Libre Baskerville", Georgia, serif;
    font-size: 28px; line-height: 30px; color: var(--white);
  }

  /* Front */
  .front-title {
    position: absolute; right: 58px; top: 372px; text-align: right;
    font-family: "Anton", Impact, sans-serif; color: var(--ink);
  }
  .front-title .line { display: block; font-size: 78px; line-height: 78px; letter-spacing: 1px; }
  .front-title .accent { color: var(--magenta); font-size: 124px; line-height: 116px; }
  .front-tagline {
    position: absolute; right: 18px; top: 660px; text-align: right;
    font-family: "Libre Baskerville", Georgia, serif;
    font-size: 26px; line-height: 33px; color: var(--ink);
  }
  .front-author {
    position: absolute; left: 810px; top: 756px;
    font-family: "Libre Baskerville", Georgia, serif;
    font-size: 34px; color: var(--plum);
  }
</style>
</head>
<body>
<main class="cover-wrap">
  <div class="sheets-photo" role="img" aria-label="Photograph of rumpled cream satin bed sheets with two pairs of bare feet entwined at the top right"></div>

  <section class="spine">
    <div class="spine-title-block">
      <span class="spine-title">The Open Map of <span class="accent">Desire</span></span>
      <span class="spine-tagline">a radical fresh perspective on intimacy, partnership and love</span>
    </div>
    <div class="spine-author-box">
      <span class="band b1"></span><span class="band b2"></span><span class="band b3"></span>
      <p class="spine-author">Marisa<br>Tolven</p>
    </div>
  </section>

  <section class="front">
    <h1 class="front-title">
      <span class="line">The Open</span>
      <span class="line">Map of</span>
      <span class="line accent">Desire</span>
    </h1>
    <p class="front-tagline">a radical fresh perspective<br>on intimacy, partnership and love</p>
    <p class="front-author">Marisa Tolven</p>
  </section>
</main>
</body>
</html>
```